Business Card Design - Law Firm

I need a business card design. I have attached a picture of the law firm's website and logo. The business card design should be consistent with those pictures. There should be a place for the employee name, employee job title, telephone number, facsimile number, address, website url, and email address for each employee.
Industry/Entity Type
Business

```html
<!DOCTYPE html>
<html lang="en">
<head>
<meta charset="utf-8">
<title>Ashcombe Law – Business Card</title>
<link rel="stylesheet" href="https://fonts.googleapis.com/css2?family=Noto+Sans:wght@400;600&display=swap">
<style>
  :root {
    --page: #e9e9ea;
    --charcoal: #4a4b4e;
    --white: #ffffff;
    --gold: #a08f3c;
    --ink: #1e1e1e;
    --text: #3a3a3a;
    --mark: #1a1a1a;
  }
  * { box-sizing: border-box; margin: 0; padding: 0; }
  html, body { width: 1200px; height: 951px; overflow: hidden; }
  body {
    background: var(--page);
    font-family: "Noto Sans", Verdana, sans-serif;
    display: flex;
    flex-direction: column;
    align-items: center;
    justify-content: center;
    gap: 50px;
  }
  .card {
    position: relative;
    width: 720px;
    height: 411px;
    box-shadow: 0 6px 18px rgba(0,0,0,0.18);
    overflow: hidden;
  }

  /* Reverse side */
  .card-back { background: var(--charcoal); }
  .card-back .band {
    position: absolute;
    left: 0; right: 0;
    top: 32%; height: 36%;
    background: var(--white);
    display: flex;
    align-items: center;
    justify-content: center;
  }

  /* Firm name lockup */
  .firm {
    display: flex;
    align-items: center;
    gap: 18px;
  }
  .firm-square {
    width: 54px; height: 54px;
    background: var(--mark);
  }
  .firm-name {
    font-size: 40px;
    font-weight: 400;
    color: var(--gold);
    letter-spacing: 0.5px;
  }

  /* Front side */
  .card-front {
    background: var(--white);
    border-left: 10px solid var(--charcoal);
    border-right: 22px solid var(--charcoal);
  }
  .card-front .firm {
    position: absolute;
    top: 62px;
    left: 50%;
    transform: translateX(-50%);
  }
  .holder {
    position: absolute;
    left: 52px; top: 200px;
  }
  .holder-name {
    font-size: 27px;
    color: var(--ink);
    font-weight: 400;
  }
  .holder-title {
    font-size: 15px;
    color: var(--gold);
  }
  .contact {
    position: absolute;
    top: 300px;
    list-style: none;
    font-size: 17px;
    line-height: 23px;
    color: var(--text);
  }
  .contact-address { left: 52px; }
  .contact-lines { left: 400px; }
  .contact li {
    display: flex;
    align-items: flex-start;
    gap: 10px;
  }
  .contact .icon {
    width: 14px; height: 14px;
    margin-top: 4px;
    flex: none;
    fill: var(--gold);
  }
  .contact .no-icon { width: 14px; flex: none; }
</style>
</head>
<body>

  <section class="card card-back" aria-label="Card reverse">
    <div class="band">
      <div class="firm">
        <span class="firm-square"></span>
        <span class="firm-name">Ashcombe Law</span>
      </div>
    </div>
  </section>

  <section class="card card-front" aria-label="Card front">
    <div class="firm">
      <span class="firm-square"></span>
      <span class="firm-name">Ashcombe Law</span>
    </div>

    <div class="holder">
      <p class="holder-name">Mara Quillen</p>
      <p class="holder-title">employee</p>
    </div>

    <ul class="contact contact-address">
      <li>
        <svg class="icon" viewBox="0 0 14 14"><path d="M7 1 L13 6.5 H11 V13 H8.5 V9 H5.5 V13 H3 V6.5 H1 Z"/></svg>
        <span>P.O. Box 40217</span>
      </li>
      <li><span class="no-icon"></span><span>Lakeview, WI 53999</span></li>
    </ul>

    <ul class="contact contact-lines">
      <li>
        <svg class="icon" viewBox="0 0 14 14"><path d="M3 1 C1.5 2 1 4 2 6.5 C3.5 10 6 12.5 9 13 C10.5 13.3 11.7 12.5 12.5 11.5 L10 9 L8.5 10 C7 9.3 5 7.2 4.2 5.5 L5.3 4 Z"/></svg>
        <span>555-014-2200</span>
      </li>
      <li>
        <svg class="icon" viewBox="0 0 14 14"><rect x="4" y="1" width="6" height="4"/><rect x="1" y="5" width="12" height="6" rx="1"/><rect x="4" y="9" width="6" height="4" fill="#fff" stroke="#a08f3c"/></svg>
        <span>555-014-2201</span>
      </li>
      <li>
        <svg class="icon" viewBox="0 0 14 14"><rect x="1" y="3" width="12" height="9" rx="1"/><path d="M1.5 3.5 L7 8 L12.5 3.5" fill="none" stroke="#fff" stroke-width="1.2"/></svg>
        <span>mara@ashcombelaw.com</span>
      </li>
      <li>
        <svg class="icon" viewBox="0 0 14 14"><circle cx="7" cy="7" r="6"/></svg>
        <span>www.ashcombelaw.com</span>
      </li>
    </ul>
  </section>

</body>
</html>
```